We need visit card and a letter paper for our website. thx

We have a beauty clinic in Switzerland.
https://wolkenbachtal.ch
We need a visit card.

Requirements
Must have
• see colors on website

```html
<!DOCTYPE html>
<html lang="de">
<head>
<meta charset="utf-8">
<title>Wolkenbachtal – Visitenkarte</title>
<link rel="stylesheet" href="https://fonts.googleapis.com/css2?family=EB+Garamond:wght@500&family=Roboto:wght@400&display=swap">
<style>
  :root {
    --backdrop: #dedede;
    --paper: #ffffff;
    --ink: #0a0a0c;
    --ink-soft: #555555;
    --card-dark: #060709;
    --on-dark: #ffffff;
  }
  * { box-sizing: border-box; margin: 0; padding: 0; }
  html, body {
    width: 1173px; height: 1200px; overflow: hidden;
    background: var(--backdrop);
  }
  .canvas { position: relative; width: 1173px; height: 1200px; }

  .card { position: absolute; left: 204px; width: 743px; height: 411px; }
  .card--front { top: 150px; background: var(--paper); }
  .card--back  { top: 637px; background: var(--card-dark); }

  .brand {
    position: absolute; display: flex; align-items: center; gap: 14px;
    font-family: "EB Garamond", serif; font-weight: 500; white-space: nowrap;
  }
  .brand__square { display: block; background: currentColor; }
  .card--front .brand { left: 56px; top: 72px; color: var(--ink); font-size: 44px; }
  .card--front .brand__square { width: 14px; height: 14px; }
  .card--back .brand {
    left: 0; right: 0; top: 168px; justify-content: center;
    color: var(--on-dark); font-size: 66px;
  }
  .card--back .brand__square { width: 18px; height: 18px; }

  .holder { position: absolute; right: 57px; top: 176px; text-align: right; }
  .holder__name {
    font-family: "EB Garamond", serif; font-weight: 500;
    font-size: 26px; color: var(--ink); line-height: 1.1;
  }
  .holder__role {
    font-family: "Roboto", sans-serif; font-size: 18.5px;
    color: var(--ink-soft); line-height: 1.2;
  }
  .tab { position: absolute; right: 0; top: 178px; width: 28px; height: 47px; background: var(--ink); }

  .contact {
    position: absolute; left: 60px; top: 236px;
    font-family: "Roboto", sans-serif; color: var(--ink-soft);
    font-size: 18.5px; line-height: 25px;
  }
  .contact__address { margin-bottom: 3px; }
  .contact__line { display: flex; align-items: center; gap: 8px; line-height: 26.5px; font-size: 19.5px; }
  .contact__icon { width: 19px; height: 17px; flex: none; color: var(--ink); }
</style>
</head>
<body>
<main class="canvas">
  <section class="card card--front">
    <div class="brand"><span class="brand__square"></span>Wolkenbachtal</div>

    <div class="holder">
      <p class="holder__name">Dr. Lindqvist Marco, DESA</p>
      <p class="holder__role">FA for anesthetist</p>
    </div>
    <div class="tab"></div>

    <div class="contact">
      <p class="contact__address">Talweg 14, 7560<br>Bergfeld, Switzerland</p>
      <p class="contact__line">
        <svg class="contact__icon" viewBox="0 0 20 18" aria-hidden="true">
          <path d="M2 6c0-3 4-4 8-4s8 1 8 4v1h-4V5.5H6V7H2z" fill="currentColor"/>
          <path d="M6 8h8l3 8H3z" fill="currentColor"/>
          <circle cx="10" cy="12" r="2" fill="#fff"/>
        </svg>+41 (0) 800 24 36 58
      </p>
      <p class="contact__line">
        <svg class="contact__icon" viewBox="0 0 20 18" aria-hidden="true">
          <path d="M1 7l9-6 9 6v10H1z" fill="currentColor"/>
          <path d="M4 5h12v5l-6 3-6-3z" fill="#fff"/>
          <path d="M6 7h8M6 9h8" stroke="currentColor" stroke-width="1"/>
        </svg>hallo@wolkenbachtal.ch
      </p>
      <p class="contact__line">
        <svg class="contact__icon" viewBox="0 0 20 18" aria-hidden="true">
          <circle cx="10" cy="9" r="7.5" fill="none" stroke="currentColor" stroke-width="1.8"/>
          <path d="M3 9h14M10 1.5c-3 3-3 12 0 15M10 1.5c3 3 3 12 0 15" fill="none" stroke="currentColor" stroke-width="1.4"/>
        </svg>www.wolkenbachtal.ch
      </p>
    </div>
  </section>

  <section class="card card--back">
    <div class="brand"><span class="brand__square"></span>Wolkenbachtal</div>
  </section>
</main>
</body>
</html>
```